Label Design for a New Alcoholized Root Beer

Create a design for a new alcoholized root beer. This is a new product category in the USA growing very rapidly. Root Beer is a popular flavor of Cola, but recently, beer manufacturers have added alcohol to it and have created a new product that has gained traction on the market at a tremendous rate.

Root Beer is vintage product that has been around for a hundred years. Consumers of this product are mostly male between the age of 30 to 45. They purchase this product for its nostalgia and vintage look and taste.

This product will be in a standard 355 mL brown bottle.

It is 5.9% abv.

The name of the product is ''Corvel's Hard Root Beer''.

We have uploaded some pictures of traditional root beers to give you an idea of the feel we want our product to have and also, the bottle the product will be filled in.

Target Market(s)

Consumers are male 30-45, same market as craft beer consumers

Industry/Entity Type

Product

Requirements
Must have
• Design must have a vintage feel to it

```html
<!DOCTYPE html>
<html lang="en">
<head>
<meta charset="utf-8">
<title>Corvel's Hard Root Beer – Label Set</title>
<link rel="stylesheet" href="https://fonts.googleapis.com/css2?family=Bodoni+Moda:wght@500;600;700&display=swap">
<style>
  :root {
    --cream: #f7e5a1;
    --ink: #1c1b1a;
    --olive: #7a6a2e;
    --ornament: #6b5a22;
    --page: #ffffff;
  }
  html, body {
    margin: 0;
    padding: 0;
    overflow: hidden;
    background: var(--page);
  }
  .canvas {
    position: relative;
    width: 1200px;
    height: 1000px;
    overflow: hidden;
    background: var(--page);
    font-family: "Bodoni Moda", "Times New Roman", serif;
  }
  .defs { position: absolute; width: 0; height: 0; }
  .neck-band {
    position: absolute;
    left: 733px;
    top: 100px;
    width: 363px;
    height: 175px;
    background: var(--cream);
  }
  .neck-label {
    position: absolute;
    left: 808px;
    top: 56px;
    width: 211px;
    height: 261px;
  }
  .body-label {
    position: absolute;
    left: 760px;
    top: 396px;
    width: 340px;
    height: 420px;
  }
  .label-name { font-weight: 600; fill: var(--ink); letter-spacing: 1px; }
  .label-premium { font-weight: 500; fill: var(--ink); letter-spacing: 5px; }
  .label-quality { font-weight: 700; fill: var(--ink); letter-spacing: 1px; }
  .label-arc-text { font-weight: 500; fill: var(--ink); letter-spacing: 6px; }
</style>
</head>
<body>
<div class="canvas">

  <svg class="defs" aria-hidden="true">
    <defs>
      <polygon id="star" points="0,-13 3.8,-4.2 12.4,-4 5.6,2 8,11 0,5.6 -8,11 -5.6,2 -12.4,-4 -3.8,-4.2" fill="var(--ink)"/>
      <path id="bottom-arc" d="M 20 210 A 150 190 0 0 0 320 210" fill="none"/>
      <g id="label-art">
        <ellipse cx="170" cy="210" rx="168" ry="208" fill="var(--cream)"/>
        <ellipse cx="170" cy="210" rx="158" ry="198" fill="none" stroke="var(--ink)" stroke-width="2.5"/>
        <ellipse cx="170" cy="225" rx="130" ry="150" fill="none" stroke="var(--olive)" stroke-width="1.6"/>

        <use href="#star" x="72" y="94"/>
        <use href="#star" x="114" y="55"/>
        <use href="#star" x="168" y="39"/>
        <use href="#star" x="220" y="55"/>
        <use href="#star" x="262" y="94"/>

        <g role="img" aria-label="Ornamental filigree crest">
          <ellipse cx="170" cy="135" rx="50" ry="32" fill="var(--ornament)" opacity="0.85"/>
        </g>

        <text class="label-name" x="170" y="232" font-size="34" text-anchor="middle">CORVEL’S HARD</text>
        <text class="label-premium" x="172" y="270" font-size="19" text-anchor="middle">PREMIUM</text>
        <text class="label-quality" x="170" y="298" font-size="16" text-anchor="middle">QUALITY</text>

        <text class="label-arc-text" font-size="24">
          <textPath href="#bottom-arc" startOffset="50%" text-anchor="middle">ROOT BEER</textPath>
        </text>
      </g>
    </defs>
  </svg>

  <div class="neck-band"></div>
  <svg class="neck-label" viewBox="0 0 340 420" role="group" aria-label="Neck label">
    <use href="#label-art"/>
  </svg>

  <svg class="body-label" viewBox="0 0 340 420" role="group" aria-label="Body label">
    <use href="#label-art"/>
  </svg>

</div>
</body>
</html>
```